Flyer-Design für Fitness
Sehr angaschierte Designerin, bin begeistert! Hat sofort alles umgesetzt wie wir es haben wollten. Sehr zu Empfehlen. Vielen dank an Marta
Zielgruppe
Wir haben uns zum Ziel gesetzt, unsere Kunden individuell, professionell und in einem angenehmen Ambiente 'in form' zu bringen.
Stundenlange Workouts waren gestern. Nutzen Sie heute die zeitsparenden Methoden von EMS, VIBRO DECK und KLU Training in Begleitung mit Persönlicher Betreuung, um ihre Ziele zu erreichen. Unsere Zielgruppe sind Männer und Frauen jeden Alters, die Wert auf ihr äußeres legen und sich gesund und fit halten wollen.
Homepage: www.trainingsraum-beispielort.de
Aufgabenstellung
Wir trainieren mit Vibro Deck, Swift Pulse Wear und KLU.
Der soll ein einmal Klapp Flyer sein.

```html
<!DOCTYPE html>
<html lang="de">
<head>
<meta charset="utf-8">
<title>Gestaltfrei Fitness – Flyer</title>
<link href="https://fonts.googleapis.com/css2?family=Montserrat:wght@800&family=Open+Sans:wght@400;600;700&display=swap" rel="stylesheet">
<style>
  :root{
    --page:#e8e8e8;
    --green:#7ab21f;
    --green-dark:#3f6f0c;
    --white:#ffffff;
    --ink:#1c1c1c;
    --photo-light:#c9ccd1;
    --photo-mid:#8b8f96;
    --photo-dark:#2a2c31;
  }
  html,body{margin:0;padding:0;width:1200px;height:1200px;overflow:hidden;background:var(--page);}
  .flyer{position:absolute;left:50px;top:320px;width:1100px;height:560px;overflow:hidden;background:var(--white);box-shadow:0 14px 30px rgba(0,0,0,.18);}
  .flyer-bg{position:absolute;inset:0;}
  .headline{position:absolute;left:38px;top:64px;margin:0;font-family:"Montserrat",sans-serif;font-weight:800;font-size:76px;line-height:.93;color:var(--white);letter-spacing:1px;opacity:.92;}
  .headline span{display:block;}
  .info{position:absolute;left:790px;top:40px;width:290px;font-family:"Open Sans",sans-serif;color:var(--white);}
  .brand{margin:0 0 28px;font-size:40px;font-weight:400;line-height:1;color:var(--white);}
  .service{margin:0 0 14px;}
  .service h2{margin:0 0 3px;font-size:17px;font-weight:700;color:var(--green-dark);}
  .service ul{margin:0;padding:0;list-style:none;}
  .service li{font-size:15px;font-weight:600;line-height:1.4;padding-left:16px;position:relative;}
  .service li::before{content:"";position:absolute;left:2px;top:8px;width:5px;height:5px;background:var(--green-dark);}
  .website{margin:18px 0 0;font-size:16px;font-weight:600;}
</style>
</head>
<body>
  <div class="flyer">
    <svg class="flyer-bg" viewBox="0 0 1100 560" width="1100" height="560">
      <defs>
        <linearGradient id="photoTraining" x1="0" y1="0" x2="1" y2="1">
          <stop offset="0" stop-color="var(--photo-light)"/>
          <stop offset=".55" stop-color="var(--photo-mid)"/>
          <stop offset="1" stop-color="var(--photo-dark)"/>
        </linearGradient>
        <linearGradient id="photoSuit" x1="1" y1="0" x2="0" y2="1">
          <stop offset="0" stop-color="#e4e5e8"/>
          <stop offset=".5" stop-color="var(--photo-mid)"/>
          <stop offset="1" stop-color="var(--photo-dark)"/>
        </linearGradient>
      </defs>
      <polygon points="0,0 440,0 360,560 0,560" fill="url(#photoTraining)" role="img" aria-label="Foto: Paar im EMS-Anzug trainiert im Studio"/>
      <polygon points="452,0 760,0 700,560 372,560" fill="url(#photoSuit)" role="img" aria-label="Foto: Mann im EMS-Anzug beim Training"/>
      <polygon points="772,0 1100,0 1100,560 712,560" fill="var(--green)"/>
    </svg>

    <h1 class="headline"><span>EMS</span><span>VIBRO</span><span>DECK</span><span>KLU</span><span>TRAINING</span></h1>

    <div class="info">
      <p class="brand">gestaltfrei Fitness</p>
      <div class="service">
        <h2>EMS</h2>
        <ul><li>Ferum et a litiae cone</li><li>Ferum et a utatempe cone</li></ul>
      </div>
      <div class="service">
        <h2>VIBRO DECK</h2>
        <ul><li>Ferum et a litiae cone</li><li>Ferum et a utatempe cone</li></ul>
      </div>
      <div class="service">
        <h2>KLU TRAINING</h2>
        <ul><li>Ferum et a litiae cone</li><li>Ferum et a utatempe cone</li></ul>
      </div>
      <p class="website">www.gestaltfrei-fitness.de</p>
    </div>
  </div>
</body>
</html>
```